company name - HARLOWMERE AIRPORT TRANSFER.
include this information please .....25 YEARS EXPERIENCE / CARS+MPVS+MINIBUSES AVAILABLE - ALL AT SAME PRICE AT ANY TIME OF DAY. NO EXTRA HIDDEN CHARGES.

PRICES [ selection ] ......

BRAXMOOR ....£100
CORVALE ....£130
DERRIN...£55.00
QUILLBOURNE ...£60.00
HALVERSTOKE ...£100.00
UPPER KESTLING ...£100,00
QUAYSIDE AIRPORT ...£95.00

```html
<!DOCTYPE html>
<html lang="en">
<head>
<meta charset="utf-8">
<title>Harlowmere Airport Transfer</title>
<link href="https://fonts.googleapis.com/css2?family=Montserrat:wght@500;600;700;800;900&display=swap" rel="stylesheet">
<style>
  :root {
    --blue-deep: #0f5fb8;
    --blue: #1c86dc;
    --blue-light: #4fb3f0;
    --ink: #111111;
    --white: #ffffff;
    --grey: #d6d8db;
    --grey-soft: #eef0f2;
  }
  * { box-sizing: border-box; margin: 0; padding: 0; }
  html, body { width: 852px; height: 1200px; overflow: hidden; background: var(--white); }
  body { font-family: "Montserrat", Arial, sans-serif; color: var(--ink); }

  .flyer { position: relative; width: 852px; height: 1200px; overflow: hidden; background: var(--white); }
  .backdrop { position: absolute; inset: 0; width: 852px; height: 1200px; }

  .brand {
    position: absolute; left: 0; right: 0; top: 62px;
    text-align: center; color: var(--white);
    font-weight: 800; font-size: 58px; line-height: 1.08; letter-spacing: 1px;
  }

  .intro { position: absolute; left: 0; right: 0; top: 352px; text-align: center; }
  .intro__headline { font-weight: 900; font-size: 47px; letter-spacing: 0.5px; line-height: 1.1; }
  .intro__line { font-weight: 600; font-size: 28px; line-height: 1.28; }
  .intro__note { font-weight: 500; font-size: 22px; line-height: 1.5; }

  .fleet {
    position: absolute; left: 104px; top: 516px; width: 650px; height: 118px;
    border-radius: 40px;
    background: linear-gradient(90deg, #c9ccd0 0%, #f2f3f4 30%, #c2c6ca 55%, #f4f5f6 80%, #dfe1e3 100%);
  }

  .price-box {
    position: absolute; left: 70px; top: 634px; width: 704px; height: 354px;
    border: 9px solid var(--blue); border-radius: 34px; background: var(--white);
    padding: 32px 80px 0 92px;
  }
  .price-row { display: flex; align-items: baseline; height: 42px; font-size: 27px; }
  .price-row__place { color: var(--blue); font-weight: 800; white-space: nowrap; }
  .price-row__dots { flex: 1; border-bottom: 4px dotted var(--ink); margin: 0 6px; transform: translateY(-6px); }
  .price-row__price { font-weight: 600; white-space: nowrap; }

  .contact {
    position: absolute; left: 518px; top: 1036px;
    color: var(--blue); font-weight: 800; font-size: 26px;
  }

  .plane { position: absolute; width: 46px; height: 24px; border-radius: 12px; }
  .plane--white { left: 258px; top: 1134px; background: var(--white); }
  .plane--blue { left: 448px; top: 1146px; background: var(--blue); }
</style>
</head>
<body>
<main class="flyer">
  <svg class="backdrop" viewBox="0 0 852 1200" aria-hidden="true">
    <defs>
      <linearGradient id="headerFill" x1="0" y1="0" x2="1" y2="1">
        <stop offset="0" stop-color="#0f5fb8"/>
        <stop offset="1" stop-color="#2a9be6"/>
      </linearGradient>
      <linearGradient id="sideFill" x1="0" y1="0" x2="1" y2="0">
        <stop offset="0" stop-color="#ffffff"/>
        <stop offset="1" stop-color="#c9ccd0"/>
      </linearGradient>
    </defs>
    <path d="M0 0 H852 V300 C700 360 520 330 360 300 C220 274 90 300 0 330 Z" fill="url(#headerFill)"/>
    <path d="M40 292 C200 232 480 208 730 226 C520 228 300 252 100 318 C70 312 52 304 40 292 Z" fill="#ffffff" opacity="0.95"/>
    <path d="M852 300 C760 360 650 380 560 370 C690 340 790 300 852 260 Z" fill="#4fb3f0"/>
    <path d="M600 600 C740 640 820 760 852 820 V1040 C780 980 700 930 600 900 Z" fill="url(#sideFill)"/>
    <path d="M0 1056 C200 1006 400 1040 580 1092 C710 1126 800 1106 852 1094 V1200 H0 Z" fill="#1c86dc"/>
    <path d="M0 1110 C220 1062 440 1092 620 1142 C730 1168 800 1152 852 1142 V1200 H0 Z" fill="#111111"/>
    <path d="M0 1164 C200 1136 420 1162 600 1192 L608 1200 H0 Z" fill="#1c86dc"/>
  </svg>

  <h1 class="brand">HARLOWMERE<br>AIRPORT TRANSFER</h1>

  <section class="intro">
    <h2 class="intro__headline">25 YEARS EXPERIENCE</h2>
    <p class="intro__line">Cars+MPVs+Minibuses available.</p>
    <p class="intro__line">All at same price at any time of day.</p>
    <p class="intro__note">No extra hidden charges.</p>
  </section>

  <div class="fleet" role="img" aria-label="Photos of a car, an MPV and a minibus"></div>

  <section class="price-box">
    <div class="price-row"><span class="price-row__place">BRAXMOOR</span><span class="price-row__dots"></span><span class="price-row__price">£100</span></div>
    <div class="price-row"><span class="price-row__place">CORVALE</span><span class="price-row__dots"></span><span class="price-row__price">£130</span></div>
    <div class="price-row"><span class="price-row__place">DERRIN</span><span class="price-row__dots"></span><span class="price-row__price">£55.00</span></div>
    <div class="price-row"><span class="price-row__place">QUILLBOURNE</span><span class="price-row__dots"></span><span class="price-row__price">£60.00</span></div>
    <div class="price-row"><span class="price-row__place">HALVERSTOKE</span><span class="price-row__dots"></span><span class="price-row__price">£100.00</span></div>
    <div class="price-row"><span class="price-row__place">UPPER KESTLING</span><span class="price-row__dots"></span><span class="price-row__price">£100,00</span></div>
    <div class="price-row"><span class="price-row__place">QUAYSIDE AIRPORT</span><span class="price-row__dots"></span><span class="price-row__price">£95.00</span></div>
  </section>

  <p class="contact">Phone details</p>

  <div class="plane plane--white" role="img" aria-label="Small aeroplane illustration"></div>
  <div class="plane plane--blue" role="img" aria-label="Small aeroplane illustration"></div>
</main>
</body>
</html>
```